" Empresa que ira prestar serviço de seguro e titulo capitalizaçao para alugueis de imoveis. Nome fantasia e endereço eletronico: Vereda Patrimonial "

```html
<!DOCTYPE html>
<html lang="pt-BR">
<head>
<meta charset="utf-8">
<title>Vereda Patrimonial — Papel Timbrado</title>
<link href="https://fonts.googleapis.com/css2?family=Cinzel:wght@400&family=Lato:wght@400&display=swap" rel="stylesheet">
<style>
  :root {
    --backdrop: #e6e6e4;
    --paper: #ffffff;
    --navy: #1d3566;
    --blue-deep: #0d3f8f;
    --blue-light: #4f9ad8;
    --mark-grey: #e4e7ee;
    --footer-ink: #22345c;
  }
  * { margin: 0; padding: 0; box-sizing: border-box; }
  html, body {
    width: 1200px;
    height: 1200px;
    overflow: hidden;
    background: var(--backdrop);
  }
  .letterhead {
    position: absolute;
    left: 228px;
    top: 60px;
    width: 744px;
    height: 1075px;
    background: var(--paper);
    overflow: hidden;
    box-shadow: 0 2px 10px rgba(0, 0, 0, 0.12);
  }
  .side-band {
    position: absolute;
    left: 0;
    top: 0;
    width: 20px;
    height: 100%;
    background: linear-gradient(90deg, var(--blue-deep) 0%, var(--blue-light) 70%, #a9cdf0 100%);
  }
  .brand {
    position: absolute;
    left: 78px;
    top: 58px;
    display: flex;
    align-items: center;
    gap: 14px;
  }
  .brand-dot {
    width: 44px;
    height: 44px;
    border-radius: 50%;
    background: var(--blue-deep);
  }
  .brand-name {
    font-family: "Cinzel", serif;
    font-weight: 400;
    font-size: 30px;
    letter-spacing: 1px;
    color: var(--navy);
  }
  .corner-disc {
    position: absolute;
    left: 360px;
    top: 560px;
    width: 552px;
    height: 552px;
    border-radius: 50%;
    background: var(--mark-grey);
  }
  .contact-footer {
    position: absolute;
    left: 220px;
    top: 918px;
    width: 360px;
    text-align: center;
    font-family: "Lato", sans-serif;
    font-size: 10.5px;
    line-height: 19px;
    color: var(--footer-ink);
  }
</style>
</head>
<body>
  <main class="letterhead">
    <div class="side-band"></div>

    <header class="brand">
      <span class="brand-dot"></span>
      <span class="brand-name">Vereda Patrimonial</span>
    </header>

    <div class="corner-disc"></div>

    <footer class="contact-footer">
      <p class="contact-phone">(11) 4000-1000</p>
      <p class="contact-web">veredapatrimonial.com.br · contato@veredapatrimonial.com.br</p>
      <p class="contact-address">Rua das Palmeiras, 120 · Centro · 01000-000</p>
    </footer>
  </main>
</body>
</html>
```